Short Line Railroad website - small company simple homepage

We are looking for someone to design a webpage/home page for our railroad. Doesn't have to be fancy, just basic contact info and links to our regional partners and government agencies. We don't do any online sales but would like a web presence that makes us look professional. We have a logo, and some pictures, but are open to purchasing pictures or other graphical elements to enhance this site. We would like links to our partners websites and emergency information. I don't know how many pages this will take??

Target Market(s)

The website is for our existing customers and their partners, potential new rail customers, regional partners like Ports or Economic Development Agencies, and government regulators. We also need emergency contact info and instructions for the general public.

Industry/Entity Type

It Company

Coding

Coded - Design and coding required

Number of Pages Required

2 page

Font styles to use
Sans Serif

Requirements
Must have
• Our logo - map of railroad and area - some photos - contact info - links to designated partners - emergency contact info and emergency instructions.
• Partners include Fenwick County Washington
• Port of Merriton (Washington)
• LNPGA
• City of Hollow Brook
• National Trackway Bureau
• MBQ
• KPLTR
• will add more when I have time
Nice to have
• It would be nice to mostly use our company colors - red, black, and white.
• Just a very professional looking website, with the option of making changes in house in the future.
Should not have
• No ads

```html
<!DOCTYPE html>
<html lang="en">
<head>
<meta charset="utf-8">
<title>Riverbend Cascade Junction Railroad</title>
<link href="https://fonts.googleapis.com/css2?family=Open+Sans:wght@400;600;700;800&family=Oswald:wght@400&family=Orbitron:wght@400;500&display=swap" rel="stylesheet">
<style>
:root{
  --red:#d32a1a;
  --red-dark:#b81f12;
  --black:#111;
  --nav:#1e1e1e;
  --white:#fff;
  --paper:#ebebeb;
  --grey:#666;
  --line:#c9c9c9;
  --footer:#4d5446;
}
*{box-sizing:border-box;margin:0;padding:0}
html,body{width:681px;height:1200px;overflow:hidden;background:var(--white)}
body{position:relative;font-family:"Open Sans",sans-serif;color:#333}
.abs{position:absolute}

/* header */
.header{left:0;top:0;width:681px;height:62px;background:linear-gradient(90deg,#a9a9a3,#c9c8c2 40%,#b8b9b1 70%,#9c9f96)}
.brand{left:120px;top:14px;display:flex;align-items:center;gap:5px}
.brand-mark{width:32px;height:32px;background:var(--red)}
.brand-name{font-weight:700;font-size:10px;line-height:13px;color:var(--red);width:110px}
.search{left:475px;top:25px;width:86px;height:16px;background:#4a4a4a;color:#ccc;font-size:5.5px;padding:5px 0 0 5px}
.search svg{position:absolute;right:4px;top:4px}
.nav{left:0;top:62px;width:681px;height:16px;background:var(--nav)}
.nav-links{left:124px;top:0;display:flex;gap:9px;font-family:"Orbitron",sans-serif;font-size:6.5px;color:var(--white);line-height:16px;letter-spacing:.2px}
.nav-social{left:462px;top:0;display:flex}
.nav-social span{width:21px;height:16px;border-left:1px solid #444;display:flex;align-items:center;justify-content:center}
.nav-social i{display:block;width:7px;height:7px}

/* hero */
.hero{left:0;top:78px;width:681px;height:220px;background:linear-gradient(120deg,#3d3a33 0%,#6b6a55 25%,#8c7f55 45%,#5f6b45 65%,#7b7a6a 85%,#4b5a3e 100%)}
.hero-arrow{top:96px}
.hero-title{left:345px;top:93px;width:218px;font-weight:700;font-size:27px;line-height:32px;color:var(--white);text-align:center;letter-spacing:.3px}
.hero-title .accent{color:var(--red)}
.hero-title hr{border:0;border-top:1.5px solid var(--white);margin:1px 0 3px}
.red-rule{left:0;width:681px;height:2px;background:var(--red)}

/* booking band */
.band{left:0;top:300px;width:681px;height:185px;background:linear-gradient(#e9e9e9,#dcdcdc)}
.band-title{top:324px;font-size:8px;font-weight:700;color:var(--red);letter-spacing:.3px}
.book{left:98px;top:341px;width:153px;height:119px;background:var(--black);color:var(--white);font-size:6px}
.book .trip{position:absolute;top:15px;font-weight:700;font-size:6.5px}
.book .lbl{position:absolute;left:9px}
.book .field{position:absolute;background:var(--white);height:12px}
.book .field::after{content:"";position:absolute;right:4px;top:5px;border:2.5px solid transparent;border-top:3px solid #555}
.btn{background:var(--red);color:var(--white);text-align:center}
.book .btn{position:absolute;left:100px;top:94px;width:45px;height:13px;font-family:"Orbitron",sans-serif;font-size:5.5px;line-height:13px}
.map{left:264px;top:341px;width:153px;height:119px;background:linear-gradient(135deg,#ece8dc,#e3dfd2 50%,#dcd8c8);border:1px solid #ccc}
.quick{left:430px;top:341px;width:153px;height:119px;background:var(--red)}
.quick .in{position:absolute;left:8px;width:137px;background:#ececec;color:#999;font-size:5.5px;padding:3px 3px}
.quick .btn{position:absolute;left:107px;top:96px;width:38px;height:13px;background:var(--black);font-family:"Orbitron",sans-serif;font-size:5.5px;line-height:13px}
.tab{left:335px;top:486px;width:11px;height:8px;background:var(--red)}

/* welcome */
.welcome{left:0;top:487px;width:681px;height:543px;background:linear-gradient(180deg,#5c6873 0%,#8c97a0 18%,#6e7a6e 50%,#5a6d48 80%,#6a6f5a 100%)}
.welcome-title{left:0;top:518px;width:681px;text-align:center;font-family:"Orbitron",sans-serif;font-size:19px;color:var(--white);letter-spacing:2px}
.panel-halo{left:70px;top:565px;width:542px;height:422px;background:rgba(255,255,255,.3)}
.panel{left:75px;top:570px;width:532px;height:412px;background:var(--white)}
.col-title{top:591px;font-family:"Oswald",sans-serif;font-size:10px;color:#222}
.col-rule{top:611px;height:1px;background:var(--red)}
.photo{display:block}
.list-box{left:98px;top:700px;width:153px;height:132px;border:1px solid #ddd;border-top:0}
.list-box ul{list-style:none;padding:12px 14px 0 7px;font-size:6.4px;line-height:9px;color:#444}
.list-box li{position:relative;padding-left:10px;margin-bottom:5px}
.list-box li::before{content:"";position:absolute;left:0;top:3px;width:3px;height:3px;border-radius:50%;background:#333}
.scroll{left:245px;top:704px;width:4px;height:124px;background:#f0f0f0}
.scroll i{position:absolute;left:0;top:4px;width:4px;height:28px;background:#c8c8c8}
.gallery-frame{left:264px;top:621px;width:154px;height:164px;border:1px solid #ccc}
.thumbs{left:264px;top:792px;display:flex;gap:2px}
.thumbs span{width:29px;height:26px;border:1px solid #bbb;background:linear-gradient(#8aa2b8,#5b7048 60%,#7a3b33)}
.about-text{left:430px;top:728px;width:156px;font-size:6.5px;line-height:9px;color:#555}
.read-more{left:430px;top:787px;width:49px;height:15px;font-size:6.5px;font-weight:700;line-height:15px}
.arrow-btn{top:868px;width:12px;height:12px;background:var(--red)}
.partners{left:98px;top:890px;width:485px;height:54px;border:2px solid #d4d4d4;background:#f6f6f6;display:flex;align-items:center;justify-content:space-around;padding:0 4px}
.partner{display:flex;align-items:center;gap:4px;font-size:7.5px;font-weight:600;color:#777}
.partner i{display:block;width:11px;height:11px;border-radius:50%;background:#999}

/* footer */
.footer{left:0;top:1032px;width:681px;height:168px;background:linear-gradient(160deg,#5a5e50,#4a5244 45%,#585a4c 75%,#3f463a)}
.f-title{top:1047px;font-family:"Oswald",sans-serif;font-size:10px;color:var(--white)}
.f-rule{top:1069px;height:1px;background:#aaa}
.f-text{font-size:6.5px;line-height:9px;color:#eee}
.f-social{left:109px;top:1138px;display:flex;gap:6px}
.f-social span{width:13px;height:13px;border:1px solid #999;background:#5d6b85}
.f-social span:nth-child(2){background:#a4574a}
.f-social span:nth-child(3){background:#4f8fb5}
.news-input{left:268px;top:1110px;width:133px;height:11px;background:#3e3e3e;color:#bbb;font-size:5.5px;padding:2px 4px}
.subscribe{left:356px;top:1127px;width:45px;height:12px;font-size:6.3px;font-weight:700;line-height:12px}
.tags{left:430px;top:1085px;width:160px;display:flex;flex-wrap:wrap;gap:3px 2px}
.tags span{border:1px solid #aaa;color:#ddd;font-size:6.5px;padding:1px 4px}
.f-bottom{left:101px;top:1165px;width:529px;height:1px;background:#888}
.up{left:101px;top:1173px;width:11px;height:10px;background:#888}
.copyright{right:51px;top:1174px;font-size:5.5px;color:#eee}
</style>
</head>
<body>

<header class="abs header">
  <div class="abs brand">
    <span class="brand-mark"></span>
    <span class="brand-name">Riverbend Cascade Junction Railroad</span>
  </div>
  <div class="abs search">Search...
    <svg width="7" height="7" viewBox="0 0 10 10"><circle cx="4" cy="4" r="3" fill="none" stroke="#fff" stroke-width="1.5"/><path d="M6.3 6.3 9 9" stroke="#fff" stroke-width="1.5"/></svg>
  </div>
</header>

<nav class="abs nav">
  <div class="abs nav-links">
    <span>Home</span><span>About us</span><span>Ride a Train</span><span>Customers</span><span>Freight</span><span>Contact us</span>
  </div>
  <div class="abs nav-social">
    <span><i style="background:#3c5a99"></i></span>
    <span><i style="background:var(--red)"></i></span>
    <span style="border-right:1px solid #444"><i style="background:#2aa3ef"></i></span>
  </div>
</nav>

<section class="abs hero" role="img" aria-label="Passenger train winding along a forested river valley in autumn">
</section>
<svg class="abs hero-arrow" style="left:14px;top:174px" width="8" height="12" viewBox="0 0 8 12"><path d="M6 1 1 6l5 5" fill="none" stroke="#fff" stroke-width="1.6"/></svg>
<svg class="abs hero-arrow" style="left:658px;top:174px" width="8" height="12" viewBox="0 0 8 12"><path d="M2 1l5 5-5 5" fill="none" stroke="#fff" stroke-width="1.6"/></svg>
<div class="abs hero-title">
  <div>A LEGEND OVER</div>
  <hr>
  <div class="accent">A 100 YEARS</div>
  <hr>
  <div>IN THE MAKING</div>
</div>
<div class="abs red-rule" style="top:298px"></div>

<section class="abs band" role="img" aria-label="Faded railway tracks background"></section>
<h2 class="abs band-title" style="left:100px">BOOK YOUR TRIP</h2>
<h2 class="abs band-title" style="left:266px">LOCATE US</h2>
<h2 class="abs band-title" style="left:432px">QUICK CONTACT</h2>

<form class="abs book">
  <span class="trip" style="left:10px"><svg width="6" height="6" viewBox="0 0 6 6" style="vertical-align:-0.5px"><circle cx="3" cy="3" r="2.3" fill="none" stroke="var(--red)" stroke-width="1"/><circle cx="3" cy="3" r="1" fill="var(--red)"/></svg> ONE WAY</span>
  <span class="trip" style="left:66px">ROUND TRIP</span>
  <span class="lbl" style="top:34px">From:</span><span class="field" style="left:30px;top:32px;width:115px"></span>
  <span class="lbl" style="top:51px">To:</span><span class="field" style="left:30px;top:49px;width:115px"></span>
  <span class="lbl" style="top:69px">Date:</span><span class="field" style="left:30px;top:67px;width:25px;background:#fff"></span>
  <span class="lbl" style="left:63px;top:69px">Adult:</span><span class="field" style="left:82px;top:67px;width:19px"></span>
  <span class="lbl" style="left:108px;top:69px">Child:</span><span class="field" style="left:126px;top:67px;width:19px"></span>
  <span class="btn">Book now</span>
</form>

<div class="abs map" role="img" aria-label="Street map of the service area with a pin marking the railroad office"></div>
<svg class="abs" style="left:319px;top:406px" width="10" height="14" viewBox="0 0 10 14"><path d="M5 13C2 8 1 6.5 1 5a4 4 0 0 1 8 0c0 1.5-1 3-4 8z" fill="var(--red)"/><circle cx="5" cy="5" r="1.5" fill="#fff"/></svg>

<form class="abs quick">
  <span class="in" style="top:9px;height:12px">Name:</span>
  <span class="in" style="top:26px;height:12px">Email:</span>
  <span class="in" style="top:43px;height:47px">Message:</span>
  <span class="btn">Submit</span>
</form>

<div class="abs red-rule" style="top:484px"></div>
<div class="abs tab"><svg width="11" height="8" viewBox="0 0 11 8"><path d="M3 5.5 5.5 3 8 5.5" fill="none" stroke="#fff" stroke-width="1.2"/></svg></div>

<section class="abs welcome" role="img" aria-label="Snow-capped mountains above a valley with a red passenger train"></section>
<h1 class="abs welcome-title">WELCOME TO RCJR</h1>
<div class="abs panel-halo"></div>
<main class="abs panel"></main>

<h3 class="abs col-title" style="left:99px">Emergency instructions</h3>
<div class="abs col-rule" style="left:98px;width:138px"></div>
<div class="abs photo" role="img" aria-label="Rail line along a lakeshore cliff" style="left:98px;top:622px;width:153px;height:78px;background:linear-gradient(110deg,#6f8fa0,#5d7a6a 45%,#4d5f3f 70%,#6a6a5e)"></div>
<div class="abs list-box">
  <ul>
    <li>Duis aute irure dolor in voluptate velit esse cillum dolore</li>
    <li>Excepteur sint occaecat cupidatat non proident</li>
    <li>Temporibus autem quibusdam et aut officiis debitis aut rerum</li>
    <li>Itaque earum rerum hic tenetur a sapiente delectus</li>
    <li>Quis autem vel eum iure qui in ea voluptate</li>
  </ul>
</div>
<div class="abs scroll"><i></i></div>

<h3 class="abs col-title" style="left:267px">Our Gallery</h3>
<div class="abs col-rule" style="left:266px;width:136px"></div>
<div class="abs gallery-frame"></div>
<div class="abs photo" role="img" aria-label="Freight train curving through a mountain valley" style="left:270px;top:627px;width:143px;height:149px;border:2px solid #555;background:linear-gradient(180deg,#8fb0cc 0%,#c8d2d8 25%,#52704a 55%,#6b7d85 80%,#7b3a2e)"></div>
<div class="abs thumbs"><span></span><span></span><span></span><span></span><span></span></div>

<h3 class="abs col-title" style="left:432px">About RCJR</h3>
<div class="abs col-rule" style="left:430px;width:137px"></div>
<div class="abs photo" role="img" aria-label="Passenger train crossing a trestle bridge over a forest river" style="left:430px;top:622px;width:153px;height:99px;background:linear-gradient(180deg,#7ea2c4 0%,#a7b9c8 25%,#3f6a3a 50%,#355a30 80%,#4e6e5a)"></div>
<p class="abs about-text">Temporibus autem quibusdam et aut officiis debitis aut rerum necessitatibus saepe eveniet ut et voluptates repudiandae sint et molestiae non recusandae. Itaque earum rerum hic tenetur a sapiente delectus ut aut reiciendis...</p>
<a class="abs btn read-more">Read More</a>

<h3 class="abs col-title" style="left:100px;top:849px">Our Partners</h3>
<div class="abs col-rule" style="left:98px;top:871px;width:92px"></div>
<div class="abs arrow-btn" style="left:554px"><svg width="12" height="12" viewBox="0 0 12 12"><path d="M7 3.5 4.5 6 7 8.5" fill="none" stroke="#fff" stroke-width="1.2"/></svg></div>
<div class="abs arrow-btn" style="left:569px"><svg width="12" height="12" viewBox="0 0 12 12"><path d="M5 3.5 7.5 6 5 8.5" fill="none" stroke="#fff" stroke-width="1.2"/></svg></div>
<div class="abs partners">
  <span class="partner"><i></i>KPLTR</span>
  <span class="partner"><i></i>LNPGA</span>
  <span class="partner"><i></i>MBQ</span>
  <span class="partner"><i></i>National Trackway Bureau</span>
  <span class="partner"><i></i>Port of Merriton</span>
</div>

<div class="abs red-rule" style="top:1030px"></div>
<footer class="abs footer" role="img" aria-label="Faded view of a red train in a mountain valley"></footer>

<h4 class="abs f-title" style="left:109px">Contact Us</h4>
<div class="abs f-rule" style="left:109px;width:132px"></div>
<svg class="abs" style="left:110px;top:1086px" width="6" height="8" viewBox="0 0 6 8"><path d="M3 7.5C1.2 4.8.5 4 .5 3a2.5 2.5 0 0 1 5 0c0 1-.7 1.8-2.5 4.5z" fill="#fff"/><circle cx="3" cy="3" r=".9" fill="#4d5446"/></svg>
<p class="abs f-text" style="left:125px;top:1083px;width:120px">2180 Alder Yard Rd Suite 40, Merriton, WA 98710, United States</p>
<svg class="abs" style="left:110px;top:1108px" width="7" height="7" viewBox="0 0 10 10"><path d="M2 1l2 2-1 1.5c.8 1.5 1.5 2.2 3 3L7.5 6l2 2-1.5 1.5C5 9 1 5 .5 2.5z" fill="#fff"/></svg>
<p class="abs f-text" style="left:125px;top:1108px">+1 555-014-2290</p>
<div class="abs f-social"><span></span><span></span><span></span></div>

<h4 class="abs f-title" style="left:266px">Newsletter</h4>
<div class="abs f-rule" style="left:266px;width:135px"></div>
<p class="abs f-text" style="left:266px;top:1083px;width:135px">Subscribe to our newsletter for latest update</p>
<div class="abs news-input">Email address...</div>
<a class="abs btn subscribe">Subscribe</a>

<h4 class="abs f-title" style="left:432px">LINKS</h4>
<div class="abs f-rule" style="left:432px;width:135px"></div>
<div class="abs tags">
  <span>News</span><span>About</span><span>Gallery</span><span>Suppliers</span>
  <span>Media</span><span>Customers</span><span style="padding:1px 9px">Partners</span>
</div>

<div class="abs f-bottom"></div>
<div class="abs up"><svg width="11" height="10" viewBox="0 0 11 10"><path d="M3 6.5 5.5 4 8 6.5" fill="none" stroke="#fff" stroke-width="1.1"/></svg></div>
<p class="abs copyright">©Copyright information here</p>

</body>
</html>
```